Tanning Lotion package label & Logo

Need hot new label for tanning lotion focusing on dark tanning. Sexy design must compete with soon to be dated but still popular "Pixie on the shelf" styles here:
http://www.plovermart.example/s/ref=nb_sb_noss_1?url=search-alias%3Daps&field-keywords=tanning%20lotion&sprefix=tanni%2Caps&rh=i%3Aaps%2Ck%3Atanning%20lotion
Have 30 days to complete. High end product needs right look.
Product name: SunBrimGlo
Target Market(s)
SunBrimGlo is a high-end, one-of-a-kind, multi-purpose Dual Glow Lotion that can be used indoors as a self-tanner, outdoors on the beach, or at tanning salons. The SunBrimGlo formula delivers a high performing silicone base to provide an excellent, non-irritating, non-oily, non-tacky, luxurious, light and greaseless overall feel on the skin when applied. This high performing silicon base also provides sebum absorption and control to help clear and prevent breakouts. SunBrimGlo contains a complex mixture of moisturizers and emollients including vitamin B5 to prevent and treat dry skin, protect sensitive skin, and improve skin tone and texture. It also contains a powerful blend of antioxidants including Grape Seed extract which is rich in OPC’s and has 20 times the antioxidant power of vitamin C, and 50 times the antioxidant power of vitamin E to help fight free radicals, protect and improve skin appearance and maintain healthy looking skin. SunBrimGlo contains a unique combination of two natural skin-tanning compounds to produce an even, deeper, and longer lasting tan. Tanning accelerators using natural amino acids help increase the production of melanin for a quicker and darker tan. SunBrimGlo is the most technologically advanced tanning lotion on the market today!
SunBrimGlo is a high-end product and will have a retail price point around $50 USD for 200 ml.
SunBrimGlo is aimed at the mid to high market
Target demographic are white girls and women aged 16-49, followed by white males aged 18-55.
SunBrimGlo will be sold online direct to consumers initially then followed by;
1. On shelves in beach area shops
2. In tanning salons
3. On shelves in mid-large box retail stores
Industry/Entity Type
Product
Look and feel
Each slider illustrates characteristics of the customer's brand and the style your logo design should communicate.

```html
<!DOCTYPE html>
<html lang="en">
<head>
<meta charset="utf-8">
<title>SunBrimGlo Dual Glow Lotion – Label</title>
<link rel="stylesheet" href="https://fonts.googleapis.com/css2?family=Roboto:wght@300;400;700&display=swap">
<style>
  :root {
    --silver-dark: #9c9c9c;
    --silver-mid: #c9c9c9;
    --silver-light: #f5f5f5;
    --panel-black: #1c1c1c;
    --ink: #1a1a1a;
    --rule: #2a2a2a;
    --paper: #ffffff;
  }
  * { margin: 0; padding: 0; box-sizing: border-box; }
  html, body {
    width: 698px;
    height: 1200px;
    overflow: hidden;
    background: var(--paper);
  }
  .label {
    position: relative;
    width: 698px;
    height: 1200px;
    background: linear-gradient(90deg,
      var(--silver-dark) 0%,
      var(--silver-mid) 14%,
      var(--silver-light) 42%,
      var(--silver-light) 58%,
      var(--silver-mid) 84%,
      var(--silver-dark) 100%);
    font-family: "Roboto", "Helvetica Neue", Arial, sans-serif;
    color: var(--ink);
  }
  .brand-panel {
    position: absolute;
    left: 114px;
    top: 0;
    width: 450px;
    height: 440px;
    background: var(--panel-black);
    display: flex;
    align-items: center;
    justify-content: center;
  }
  .brand-name {
    font-family: "Roboto", "Helvetica Neue", Arial, sans-serif;
    font-weight: 400;
    font-size: 38px;
    letter-spacing: 2px;
    color: var(--paper);
  }
  .product-info {
    position: absolute;
    left: 67px;
    top: 610px;
    width: 550px;
  }
  .product-name {
    font-weight: 700;
    font-size: 38px;
    line-height: 46px;
    letter-spacing: 1px;
    text-transform: uppercase;
  }
  .product-type {
    margin-top: 22px;
    padding: 16px 0 18px;
    border-top: 3px solid var(--rule);
    border-bottom: 3px solid var(--rule);
    font-weight: 400;
    font-size: 40px;
    line-height: 46px;
  }
  .product-claim {
    margin-top: 18px;
    font-weight: 300;
    font-size: 34px;
    line-height: 42px;
  }
</style>
</head>
<body>
  <main class="label">
    <section class="brand-panel">
      <span class="brand-name">SunBrimGlo</span>
    </section>
    <section class="product-info">
      <h1 class="product-name">Dual<br>Glow<br>Lotion</h1>
      <p class="product-type">Self Tanner</p>
      <p class="product-claim">contains a complex<br>mixture of<br>moisturizers<br>and emollients</p>
    </section>
  </main>
</body>
</html>
```